New Consulting Firm News PowerPoint Template

We are a new consulting firm that specializes in Veltrix Unified Results Planning implementations in need of a new PowerPoint template. We need at least the following layouts:
• Main Cover Slide
• Agenda / Table of Contents
• Title slide for each of the agenda items leading into actual content
• Title + Content with nice bullets in the content
• Title + Sub-Title + Content with nice bullets in the content
• Title + Two Columns of Content
• Title + Sub-Title + Two Columns of Content
• Title + Three Columns of Content
• Title + Sub-Title + Three Columns of Content
• Title + Two Rows and Two Columns of Content (4 boxes)
• Title + Sub-Title + Two Rows and Two Columns of Content (4 boxes)
• Title + Blank
• Nascar Slide (Client logos arranged somehow)
• Case Study Slide
• Various infographic slides than can be used and modified would be amazing as well
Our logo has been uploaded and you can find our website here:
https://brankelladvisory.example
We would like the main theme colors to blend with our logo, but also have a variety of colors in the theme that compliment the main theme colors. Once we have selected a PowerPoint design we expect to immediately have a Word design contest and the winning PowerPoint design will likely be a heavy influence on the Word design.

Target Market(s)

CFO, CAO, VP of Finance, Controllers

Industry/Entity Type

Consulting

Font styles to use
Serif
Sans Serif

Requirements
Must have
• • Main Cover Slide
• Title + Blank
• Case Study Slide
Nice to have
• • Various infographic slides than can be used and modified would be amazing as well

```html
<!DOCTYPE html>
<html lang="en">
<head>
<meta charset="utf-8">
<title>Brankell Advisory – Presentation Template</title>
<link href="https://fonts.googleapis.com/css2?family=Montserrat:wght@300;400;500;600;700;800&display=swap" rel="stylesheet">
<style>
:root{
  --blue:#2f7cc4;
  --blue-deep:#1565c0;
  --ink:#222;
  --gray:#8c8c8c;
  --gray-dark:#555;
  --gray-light:#dedede;
  --text:#5a5a5a;
  --bg-top:#b4cfe8;
  --bg-bottom:#ffffff;
}
*{box-sizing:border-box;margin:0;padding:0}
html,body{width:1200px;height:2194px;overflow:hidden}
body{font-family:"Montserrat",sans-serif;background:#fff;position:relative}
.stage{position:absolute;left:0;top:0;width:1409px;height:2576px;transform:scale(.85167);transform-origin:0 0;
  background:linear-gradient(180deg,var(--bg-top) 0%,#cfe0f0 30%,#e9f1f8 65%,var(--bg-bottom) 100%)}
.brand{position:absolute;left:0;width:1409px;top:215px;text-align:center;color:var(--blue)}
.brand .sq{display:block;width:74px;height:74px;margin:0 auto 26px;background:var(--blue)}
.brand .name{font-weight:500;font-size:46px;letter-spacing:6px;line-height:1.1}
.brand .name small{display:block;font-size:16px;letter-spacing:8px}

.slide{position:absolute;width:425px;height:238px;background:#fff;box-shadow:0 6px 14px rgba(40,70,110,.22);overflow:hidden}
.slide>*{position:absolute}
.panel{background:var(--blue)}
.panel-gray{background:var(--gray)}
.mark{font-weight:700;font-size:5px;letter-spacing:.6px;color:var(--blue)}
.on-blue .mark,.mark.w{color:#fff}
.ptitle{font-weight:800;font-size:10.5px;line-height:10.5px;color:#fff;text-transform:uppercase}
.ptitle.dark{color:var(--ink)}
.dash{width:12px;height:1.5px;background:#fff}
.dash.dark{background:var(--ink)}
.lorem{font-size:4.3px;line-height:6.3px;color:#fff;text-align:justify}
.lorem.dark{color:var(--text)}
.foot{left:28px;right:14px;bottom:4px;display:flex;justify-content:space-between;font-size:2.8px;color:#999}
.foot span:nth-child(2){margin-right:160px}
.item{padding-left:18px;width:120px}
.item .pill{position:absolute;left:0;top:1px;width:6px;height:13px;border-radius:3px;background:var(--blue)}
.item b{display:block;font-weight:500;font-size:5.5px;letter-spacing:.3px;color:var(--gray-dark);margin-bottom:2px}
.item p{font-size:4.3px;line-height:6px;color:var(--text)}
.item.w .pill{background:#fff}
.item.w b,.item.w p{color:#fff}
.item.n{padding-left:14px;width:82px}
.list{font-size:4.4px;line-height:7.6px;color:var(--gray-dark);font-weight:600;list-style:none;width:185px}
.list li span{color:var(--blue);display:inline-block;width:16px}
.cols{display:flex;gap:10px}
.cols .lorem{flex:1}
.num{color:#fff;font-weight:600;font-size:11px}
.icon-t{font-size:5px;color:#fff;text-align:center;width:70px}
.icon-t b{display:block;font-weight:500;font-size:5.5px;margin:3px 0 2px}
.th{background:var(--blue-deep);color:#fff;font-weight:600;font-size:5px;display:flex;align-items:center;justify-content:center}
.rh{background:var(--gray);color:#fff;font-weight:600;font-size:5px;display:flex;align-items:center;padding-left:8px}
.cell{background:var(--gray-light)}
.logo-v{font-weight:700;font-size:7px;color:var(--gray-dark);letter-spacing:.5px;transform:translateX(-50%)}
.logo-b{font-weight:700;font-size:7px;color:var(--blue);letter-spacing:.5px;transform:translateX(-50%)}
.ring-label{font-weight:700;font-size:3.8px;color:var(--blue);letter-spacing:.4px;transform:translateX(-50%)}
.box{color:#fff;font-size:4.2px;line-height:5.5px;border-radius:4px;padding:5px 8px;text-align:center}
.box b{font-size:5px;font-weight:600;display:block}
</style>
</head>
<body>
<div class="stage">

  <div class="brand"><span class="sq"></span><div class="name">BRANKELL<small>ADVISORY</small></div></div>

  <!-- Row 1 -->
  <section class="slide" style="left:39px;top:432px">
    <div role="img" aria-label="soft grey abstract pattern of raised white squares" style="left:0;top:0;width:425px;height:238px;background:linear-gradient(120deg,#ececec 0%,#f5f5f5 45%,#e3e3e3 70%,#f7f7f7 100%)"></div>
    <div class="mark" style="left:30px;top:130px;font-size:15px;letter-spacing:1.5px">BRANKELL</div>
    <div class="mark" style="left:48px;top:150px;font-size:6px;letter-spacing:2px;color:var(--blue)">ADVISORY</div>
    <div style="left:160px;top:96px;width:225px;text-align:center;font-weight:300;font-size:14px;line-height:15px;color:#555">YOU CAN PLACE YOUR TITLE PRESENTATION HERE</div>
    <div style="left:160px;top:135px;width:225px;text-align:center;font-weight:700;font-size:4.6px;color:#444">YOUR SUBTITLE PRESENTATION TITLE GOES HERE</div>
    <div style="left:160px;top:162px;width:225px;text-align:center;font-weight:600;font-size:4.6px;color:#444">MARCH, 20 2021</div>
  </section>

  <section class="slide" style="left:492px;top:432px">
    <div class="panel on-blue" style="left:11px;top:11px;width:186px;height:217px"></div>
    <div class="mark w" style="left:28px;top:26px">BRANKELL</div>
    <div class="ptitle" style="left:30px;top:116px;width:140px">Title content with bullets in the content</div>
    <div class="dash" style="left:30px;top:158px"></div>
    <p class="lorem" style="left:30px;top:166px;width:140px">Lorem ipsum sit lom dolor sit amet, consectetur sit amet adipiscing. Lorem ipsum sit lom dolor. Lorem ipsum.</p>
    <ol class="list" style="left:215px;top:33px">
      <li><span>01.</span>TITLE + CONTENT WITH NICE BULLETS IN THE CONTENT</li>
      <li><span>02.</span>TITLE + SUB-TITLE + CONTENT WITH NICE BULLETS</li>
      <li><span>03.</span>TITLE + TWO COLUMNS OF CONTENT</li>
      <li><span>04.</span>TITLE + THREE COLUMNS OF CONTENT</li>
      <li><span>05.</span>TITLE + SUB-TITLE + THREE COLUMNS OF CONTENT</li>
      <li><span>06.</span>TITLE + THREE COLUMNS OF CONTENT</li>
      <li><span>07.</span>TITLE + SUB-TITLE + THREE COLUMNS OF CONTENT</li>
      <li><span>08.</span>TITLE + TWO ROWS AND TWO COLUMNS (4 BOXES)</li>
      <li><span>09.</span>TITLE + SUB-TITLE + TWO ROWS AND TWO COLUMNS</li>
      <li><span>10.</span>TITLE + BLANK</li>
      <li><span>11.</span>NASCAR SLIDE (CLIENT LOGOS)</li>
      <li><span>12.</span>CASE STUDY SLIDE</li>
      <li><span>13.</span>DATA TABLES</li>
      <li><span>14.</span>EDITABLE INFOGRAPHIC SLIDES</li>
    </ol>
    <div class="foot"><span>brankelladvisory.example</span><span>CONFIDENTIAL</span><span>2</span></div>
  </section>

  <section class="slide" style="left:946px;top:432px">
    <div class="panel" style="left:11px;top:11px;width:186px;height:217px"></div>
    <div class="mark w" style="left:28px;top:26px">BRANKELL</div>
    <div class="ptitle" style="left:30px;top:116px;width:140px">Title content with bullets in the content</div>
    <div class="dash" style="left:30px;top:158px"></div>
    <p class="lorem" style="left:30px;top:166px;width:140px">Lorem ipsum sit lom dolor sit amet, consectetur sit amet adipiscing. Lorem ipsum sit lom dolor. Lorem ipsum.</p>
    <div class="item" style="left:245px;top:30px"><i class="pill"></i><b>INSERT TITLE HERE</b><p>Lorem ipsum sit lom dolor sit amet, consectetur sit amet. Lorem.</p></div>
    <div class="item" style="left:245px;top:81px"><i class="pill"></i><b>INSERT TITLE HERE</b><p>Lorem ipsum sit lom dolor sit amet, consectetur sit amet. Lorem.</p></div>
    <div class="item" style="left:245px;top:132px"><i class="pill"></i><b>INSERT TITLE HERE</b><p>Lorem ipsum sit lom dolor sit amet, consectetur sit amet. Lorem.</p></div>
    <div class="item" style="left:245px;top:183px"><i class="pill"></i><b>INSERT TITLE HERE</b><p>Lorem ipsum sit lom dolor sit amet, consectetur sit amet. Lorem.</p></div>
    <div class="foot"><span>brankelladvisory.example</span><span>CONFIDENTIAL</span><span>3</span></div>
  </section>

  <!-- Row 2 -->
  <section class="slide" style="left:39px;top:718px">
    <div class="mark" style="left:30px;top:28px">BRANKELL</div>
    <div class="ptitle dark" style="left:30px;top:116px;width:140px">Title content with bullets in the content</div>
    <div class="dash dark" style="left:30px;top:158px"></div>
    <p class="lorem dark" style="left:30px;top:166px;width:120px">Lorem ipsum sit lom dolor sit amet, consectetur sit amet adipiscing. Lorem ipsum sit lom dolor. Lorem ipsum.</p>
    <div class="panel" style="left:184px;top:11px;width:229px;height:217px"></div>
    <div class="item w" style="left:245px;top:50px"><i class="pill"></i><b>INSERT TITLE HERE</b><p>Lorem ipsum sit lom dolor sit amet, consectetur sit amet. Lorem.</p></div>
    <div class="item w" style="left:245px;top:100px"><i class="pill"></i><b>INSERT TITLE HERE</b><p>Lorem ipsum sit lom dolor sit amet, consectetur sit amet. Lorem.</p></div>
    <div class="item w" style="left:245px;top:150px"><i class="pill"></i><b>INSERT TITLE HERE</b><p>Lorem ipsum sit lom dolor sit amet, consectetur sit amet. Lorem.</p></div>
    <div class="foot"><span>brankelladvisory.example</span><span>CONFIDENTIAL</span><span>4</span></div>
  </section>

  <section class="slide" style="left:492px;top:728px">
    <div class="mark" style="left:30px;top:28px">BRANKELL</div>
    <div class="ptitle dark" style="left:30px;top:104px;width:140px">Title content with bullets in the content &amp; subtitle</div>
    <div class="dash dark" style="left:30px;top:157px"></div>
    <p class="lorem dark" style="left:30px;top:165px;width:120px">Lorem ipsum sit lom dolor sit amet, consectetur sit amet adipiscing. Lorem ipsum sit lom dolor. Lorem ipsum.</p>
    <div class="panel" style="left:184px;top:11px;width:229px;height:217px"></div>
    <div class="item w n" style="left:202px;top:28px"><i class="pill"></i><b>INSERT TITLE HERE</b><p>Lorem ipsum sit lom dolor sit amet, consectetur sit amet. Lorem.</p></div>
    <div class="item w n" style="left:300px;top:28px"><i class="pill"></i><b>INSERT TITLE HERE</b><p>Lorem ipsum sit lom dolor sit amet, consectetur sit amet. Lorem.</p></div>
    <div class="item w n" style="left:202px;top:95px"><i class="pill"></i><b>INSERT TITLE HERE</b><p>Lorem ipsum sit lom dolor sit amet, consectetur sit amet. Lorem.</p></div>
    <div class="item w n" style="left:300px;top:95px"><i class="pill"></i><b>INSERT TITLE HERE</b><p>Lorem ipsum sit lom dolor sit amet, consectetur sit amet. Lorem.</p></div>
    <div class="item w n" style="left:202px;top:162px"><i class="pill"></i><b>INSERT TITLE HERE</b><p>Lorem ipsum sit lom dolor sit amet, consectetur sit amet. Lorem.</p></div>
    <div class="item w n" style="left:300px;top:162px"><i class="pill"></i><b>INSERT TITLE HERE</b><p>Lorem ipsum sit lom dolor sit amet, consectetur sit amet. Lorem.</p></div>
    <div class="foot"><span>brankelladvisory.example</span><span>CONFIDENTIAL</span><span>5</span></div>
  </section>

  <section class="slide" style="left:946px;top:730px">
    <div class="mark" style="left:30px;top:28px">BRANKELL</div>
    <div class="ptitle dark" style="left:30px;top:96px;width:110px">Title columns content (w/bullet simple text)</div>
    <div class="dash dark" style="left:30px;top:160px"></div>
    <p class="lorem dark" style="left:30px;top:168px;width:90px">Lorem ipsum sit lom dolor sit amet, consectetur sit amet adipiscing. Lorem ipsum sit lom dolor. Lorem ipsum.</p>
    <div class="panel" style="left:149px;top:11px;width:264px;height:217px"></div>
    <p class="lorem" style="left:168px;top:36px;width:112px">Lorem ipsum dolor sit amet, consectetur adipiscing elit, sed do eiusmod tempor incididunt ut labore et dolore magna aliqua. Ut enim ad minim veniam, quis nostrud exercitation ullamco laboris nisi ut aliquip ex ea commodo consequat. Duis aute irure dolor in reprehenderit in voluptate velit.<br><br>Lorem ipsum dolor sit amet, consectetur adipiscing elit, sed do eiusmod tempor incididunt ut labore. Lorem ipsum dolor sit amet, consectetur adipiscing elit, sed do eiusmod tempor incididunt ut labore et dolore magna aliqua. Ut enim ad minim, eiusmod tempor incididunt ut labore.</p>
    <div class="item w n" style="left:288px;top:48px;width:120px"><i class="pill"></i><b>INSERT TITLE HERE</b><p>Lorem ipsum sit lom dolor sit amet, consectetur sit amet. Lorem.</p></div>
    <div class="item w n" style="left:288px;top:106px;width:120px"><i class="pill"></i><b>INSERT TITLE HERE</b><p>Lorem ipsum sit lom dolor sit amet, consectetur sit amet. Lorem.</p></div>
    <div class="item w n" style="left:288px;top:164px;width:120px"><i class="pill"></i><b>INSERT TITLE HERE</b><p>Lorem ipsum sit lom dolor sit amet, consectetur sit amet. Lorem.</p></div>
    <div class="foot"><span>brankelladvisory.example</span><span>CONFIDENTIAL</span><span>6</span></div>
  </section>

  <!-- Row 3 -->
  <section class="slide" style="left:39px;top:1030px">
    <div class="mark" style="left:30px;top:28px">BRANKELL</div>
    <div class="ptitle dark" style="left:30px;top:106px;width:110px">Title two columns content (w subtitle)</div>
    <div class="dash dark" style="left:30px;top:152px"></div>
    <p class="lorem dark" style="left:30px;top:160px;width:90px">Lorem ipsum sit lom dolor sit amet, consectetur sit amet adipiscing. Lorem ipsum sit lom dolor. Lorem ipsum.</p>
    <div class="panel" style="left:149px;top:11px;width:264px;height:217px"></div>
    <div class="cols" style="left:168px;top:36px;width:228px">
      <p class="lorem">Lorem ipsum dolor sit amet, consectetur adipiscing elit, sed do eiusmod tempor incididunt ut labore et dolore magna aliqua. Ut enim ad minim veniam, quis nostrud exercitation ullamco laboris nisi ut aliquip ex ea commodo consequat. Duis aute irure dolor in reprehenderit in voluptate velit.<br><br>Lorem ipsum dolor sit amet, consectetur adipiscing elit, sed do eiusmod tempor incididunt ut labore. Lorem ipsum dolor sit amet, consectetur adipiscing elit, sed do eiusmod tempor incididunt ut labore et dolore magna aliqua. Ut enim ado, consectetur adipiscing elit.</p>
      <p class="lorem">Lorem ipsum dolor sit amet, consectetur adipiscing elit, sed do eiusmod tempor incididunt ut labore et dolore magna aliqua. Ut enim ad minim veniam.<br><br>Quis nostrud exercitation ullamco laboris nisi ut aliquip ex ea commodo consequat. Duis aute irure dolor in reprehenderit in voluptate velit.<br><br>Lorem ipsum dolor sit amet, consectetur adipiscing elit, sed do eiusmod tempor incididunt ut labore. Lorem ipsum dolor sit amet, consectetur adipiscing elit, sed do eiusmod tempor incididunt ut labore et dolore magna aliqua.</p>
    </div>
    <div class="foot"><span>brankelladvisory.example</span><span>CONFIDENTIAL</span><span>7</span></div>
  </section>

  <section class="slide" style="left:492px;top:1026px">
    <div class="panel" style="left:11px;top:11px;width:177px;height:217px"></div>
    <div class="mark w" style="left:28px;top:26px">BRANKELL</div>
    <div class="ptitle" style="left:30px;top:104px;width:140px">Title content with bullets in the content &amp; subtitle</div>
    <div class="dash" style="left:30px;top:157px"></div>
    <p class="lorem" style="left:30px;top:165px;width:140px">Lorem ipsum sit lom dolor sit amet, consectetur sit amet adipiscing. Lorem ipsum sit lom dolor. Lorem ipsum.</p>
    <div class="item n" style="left:210px;top:28px"><i class="pill"></i><b>INSERT TITLE HERE</b><p>Lorem ipsum sit lom dolor sit amet, consectetur sit amet. Lorem.</p></div>
    <div class="item n" style="left:312px;top:28px"><i class="pill"></i><b>INSERT TITLE HERE</b><p>Lorem ipsum sit lom dolor sit amet, consectetur sit amet. Lorem.</p></div>
    <div class="item n" style="left:210px;top:96px"><i class="pill"></i><b>INSERT TITLE HERE</b><p>Lorem ipsum sit lom dolor sit amet, consectetur sit amet. Lorem.</p></div>
    <div class="item n" style="left:312px;top:96px"><i class="pill"></i><b>INSERT TITLE HERE</b><p>Lorem ipsum sit lom dolor sit amet, consectetur sit amet. Lorem.</p></div>
    <div class="item n" style="left:210px;top:164px"><i class="pill"></i><b>INSERT TITLE HERE</b><p>Lorem ipsum sit lom dolor sit amet, consectetur sit amet. Lorem.</p></div>
    <div class="item n" style="left:312px;top:164px"><i class="pill"></i><b>INSERT TITLE HERE</b><p>Lorem ipsum sit lom dolor sit amet, consectetur sit amet. Lorem.</p></div>
    <div class="foot"><span>brankelladvisory.example</span><span>CONFIDENTIAL</span><span>8</span></div>
  </section>

  <section class="slide" style="left:946px;top:1024px">
    <div class="mark" style="left:30px;top:28px">BRANKELL</div>
    <div class="ptitle dark" style="left:30px;top:108px;width:100px">Title + three columns of content</div>
    <div class="dash dark" style="left:30px;top:152px"></div>
    <p class="lorem dark" style="left:30px;top:160px;width:82px">Lorem ipsum sit lom dolor sit amet, consectetur sit amet adipiscing. Lorem ipsum sit lom dolor. Lorem ipsum.</p>
    <div class="panel" style="left:131px;top:11px;width:282px;height:217px"></div>
    <div class="cols" style="left:150px;top:36px;width:245px">
      <p class="lorem">Lorem ipsum dolor sit amet, consectetur adipiscing elit, sed do eiusmod tempor incididunt ut labore et dolore magna aliqua. Ut enim ad minim veniam. Quis nostrud exercitation ullamco laboris nisi ut aliquip ex ea commodo consequat.<br><br>Duis aute irure dolor in reprehenderit in voluptate velit. Lorem ipsum dolor sit amet, consectetur adipiscing elit, sed do eiusmod tempor incididunt ut labore lorem</p>
      <p class="lorem">Lorem ipsum dolor sit amet, consectetur adipiscing elit, sed do eiusmod tempor incididunt ut labore et dolore magna aliqua. Ut enim ad minim veniam. Quis nostrud exercitation ullamco laboris nisi ut aliquip ex ea commodo consequat. Duis aute irure dolor in reprehenderit in voluptate velit.<br><br>Lorem ipsum dolor sit amet, consectetur adipiscing elit, sed do eiusmod tempor incididunt ut labore lorem</p>
      <p class="lorem">Lorem ipsum dolor sit amet, consectetur adipiscing elit, sed do eiusmod tempor incididunt ut labore et dolore magna aliqua. Ut enim ad minim veniam.<br><br>Quis nostrud exercitation ullamco laboris nisi ut aliquip ex ea commodo consequat. Duis aute irure dolor in reprehenderit in voluptate velit. Lorem ipsum dolor sit amet, consectetur adipiscing elit, sed do eiusmod.</p>
    </div>
    <div class="foot"><span>brankelladvisory.example</span><span>CONFIDENTIAL</span><span>9</span></div>
  </section>

  <!-- Row 4 -->
  <section class="slide" style="left:39px;top:1318px">
    <svg style="left:0;top:0" width="425" height="238" viewBox="0 0 425 238">
      <polygon points="11,11 250,11 190,228 11,228" fill="var(--blue)"/>
      <polygon points="250,11 292,11 232,228 190,228" fill="#9a9a9a"/>
    </svg>
    <div class="mark w" style="left:28px;top:26px">BRANKELL</div>
    <div class="ptitle" style="left:30px;top:74px;width:110px">Four points features w/ icons</div>
    <p class="lorem" style="left:30px;top:112px;width:140px">Lorem ipsum sit lom dolor sit amet, consectetur sit amet adipiscing. Lorem ipsum sit lom dolor. Lorem ipsum.<br><br>Lorem ipsum sit lom dolor sit amet, consectetur sit amet adipiscing. Lorem ipsum sit lom dolor. Lorem ipsum.</p>
    <div class="num" style="left:245px;top:46px">1</div>
    <div class="num" style="left:233px;top:84px">2</div>
    <div class="num" style="left:220px;top:122px">3</div>
    <div class="num" style="left:207px;top:160px">4</div>
    <div class="item" style="left:276px;top:45px;padding-left:0;width:120px"><b>INSERT TITLE HERE</b><p>Lorem ipsum sit lom dolor sit amet, consectetur sit amet.</p></div>
    <div class="item" style="left:264px;top:83px;padding-left:0;width:120px"><b>INSERT TITLE HERE</b><p>Lorem ipsum sit lom dolor sit amet, consectetur sit amet.</p></div>
    <div class="item" style="left:252px;top:121px;padding-left:0;width:120px"><b>INSERT TITLE HERE</b><p>Lorem ipsum sit lom dolor sit amet, consectetur sit amet.</p></div>
    <div class="item" style="left:240px;top:159px;padding-left:0;width:140px"><b>INSERT TITLE HERE</b><p>Lorem ipsum sit lom dolor sit amet, consectetur sit amet. Lorem ipsum sit lom dolor sit amet, consectetur sit amet.</p></div>
    <div class="foot"><span>brankelladvisory.example</span><span>CONFIDENTIAL</span><span>10</span></div>
  </section>

  <section class="slide" style="left:492px;top:1326px">
    <div role="img" aria-label="light grey abstract pattern of raised white squares" style="left:0;top:0;width:425px;height:238px;background:linear-gradient(110deg,#e4e4e4 0%,#f4f4f4 50%,#e9e9e9 100%)"></div>
    <svg style="left:0;top:0" width="425" height="238" viewBox="0 0 425 238">
      <polygon points="0,18 330,18 270,238 0,238" fill="var(--blue)" opacity=".93"/>
      <g fill="#8f8f8f" stroke="#fff" stroke-width="2"><circle cx="312" cy="70" r="12"/><circle cx="300" cy="108" r="12"/><circle cx="288" cy="146" r="12"/></g>
      <g fill="none" stroke="#fff" stroke-width="1.2"><rect x="306" y="65" width="12" height="8"/><path d="M300 102 v6 h6 A6 6 0 1 1 300 102"/><rect x="283" y="141" width="10" height="8"/></g>
    </svg>
    <div class="mark w" style="left:28px;top:26px">BRANKELL</div>
    <div class="ptitle" style="left:30px;top:56px;width:100px">Multiple info slide</div>
    <p class="lorem" style="left:30px;top:94px;width:70px">Lorem ipsum sit lom dolor sit amet, consectetur sit amet adipiscing.<br><br>Lorem ipsum sit lom dolor sit amet, consectetur sit amet adipiscing.<br><br>Lorem ipsum sit lom dolor sit amet, consectetur sit amet adipiscing.</p>
    <div class="num" style="left:136px;top:50px">1</div>
    <div class="num" style="left:136px;top:92px">2</div>
    <div class="num" style="left:136px;top:134px">3</div>
    <div class="item w" style="left:146px;top:54px;width:110px"><b>INSERT TITLE HERE</b><p>Lorem ipsum sit lom dolor sit amet, consectetur sit amet. Lorem ipsum sit lom.</p></div>
    <div class="item w" style="left:146px;top:96px;width:110px"><b>INSERT TITLE HERE</b><p>Lorem ipsum sit lom dolor sit amet, consectetur sit amet. Lorem ipsum sit lom.</p></div>
    <div class="item w" style="left:146px;top:138px;width:110px"><b>INSERT TITLE HERE</b><p>Lorem ipsum sit lom dolor sit amet, consectetur sit amet. Lorem ipsum sit lom.</p></div>
    <div class="item" style="left:330px;top:64px;padding-left:0;width:60px"><b>TITLE HERE</b><p>Lorem ipsum sit lom dolor sit amet, consectetur.</p></div>
    <div class="item" style="left:318px;top:102px;padding-left:0;width:80px"><b>INSERT TITLE HERE</b><p>Lorem ipsum sit lom dolor sit amet, consectetur sit amet.</p></div>
    <div class="item" style="left:306px;top:140px;padding-left:0;width:100px"><b>INSERT TITLE HERE</b><p>Lorem ipsum sit lom dolor sit amet, consectetur sit amet.</p></div>
    <div class="foot"><span></span><span></span><span>11</span></div>
  </section>

  <section class="slide" style="left:946px;top:1324px">
    <div role="img" aria-label="light grey abstract pattern of raised white squares" style="left:180px;top:0;width:245px;height:238px;background:linear-gradient(120deg,#f3f3f3 0%,#e2e2e2 55%,#f1f1f1 100%)"></div>
    <div class="mark" style="left:30px;top:28px">BRANKELL</div>
    <div class="panel" style="left:19px;top:53px;width:382px;height:150px"></div>
    <div class="ptitle" style="left:30px;top:94px;width:120px">Features slide with icons</div>
    <p class="lorem" style="left:30px;top:128px;width:120px">Lorem ipsum sit lom dolor sit amet, consectetur sit amet adipiscing. Lorem ipsum sit lom dolor. Lorem ipsum.</p>
    <svg style="left:180px;top:60px" width="220" height="120" viewBox="0 0 220 120">
      <g fill="none" stroke="#fff" stroke-width="1.2"><circle cx="52" cy="10" r="5"/><circle cx="52" cy="10" r="2"/><circle cx="139" cy="10" r="5"/><path d="M139 5 v5 h5"/><path d="M48 63 h8 M48 75 h8 M49 63 l6 12 M55 63 l-6 12"/><circle cx="139" cy="67" r="5"/></g>
    </svg>
    <div class="icon-t" style="left:197px;top:75px"><b>TITLE HERE</b>Sed ut perspiciatis unde omnis iste natus error</div>
    <div class="icon-t" style="left:284px;top:75px"><b>TITLE HERE</b>Sed ut perspiciatis unde omnis iste natus error sit</div>
    <div class="icon-t" style="left:197px;top:133px"><b>TITLE HERE</b>Sed ut perspiciatis unde omnis iste natus error</div>
    <div class="icon-t" style="left:284px;top:133px"><b>TITLE HERE</b>Sed ut perspiciatis unde omnis iste natus error</div>
    <div class="foot"><span>brankelladvisory.example</span><span>CONFIDENTIAL</span><span>12</span></div>
  </section>

  <!-- Row 5 -->
  <section class="slide" style="left:39px;top:1617px">
    <div class="panel" style="left:11px;top:11px;width:200px;height:217px"></div>
    <div role="img" aria-label="photo of hands holding a newspaper beside a cup of tea, a magnifying glass and a phone" style="left:211px;top:11px;width:202px;height:217px;background:linear-gradient(150deg,#cfd3d4 0%,#8d9497 45%,#4f5456 100%)"></div>
    <div class="mark w" style="left:28px;top:26px">BRANKELL</div>
    <div class="ptitle" style="left:30px;top:70px;width:160px">Bullets with images</div>
    <div class="num" style="left:56px;top:94px">1</div>
    <div class="num" style="left:56px;top:126px">2</div>
    <div class="num" style="left:56px;top:158px">3</div>
    <p class="lorem" style="left:76px;top:96px;width:78px">Lorem ipsum sit lom dolor sit amet, consectetur. Lorem ipsum sit lom dolor.</p>
    <p class="lorem" style="left:76px;top:128px;width:78px">Lorem ipsum sit lom dolor sit amet, consectetur. Lorem ipsum sit lom dolor.</p>
    <p class="lorem" style="left:76px;top:160px;width:78px">Lorem ipsum sit lom dolor sit amet, consectetur. Lorem ipsum sit lom dolor.</p>
    <div class="foot"><span>brankelladvisory.example</span><span>CONFIDENTIAL</span><span>13</span></div>
  </section>

  <section class="slide" style="left:492px;top:1617px">
    <div class="mark" style="left:30px;top:28px">BRANKELL</div>
    <div class="th" style="left:72px;top:55px;width:90px;height:24px">Columns 1</div>
    <div class="th" style="left:163px;top:55px;width:94px;height:24px">Columns 2</div>
    <div class="rh" style="left:28px;top:83px;width:44px;height:61px">Rows 1</div>
    <div class="rh" style="left:28px;top:145px;width:44px;height:62px">Rows 2</div>
    <div class="cell" style="left:72px;top:79px;width:185px;height:128px;background:linear-gradient(90deg,#e0e0e0 0 90px,#d6d6d6 90px 91px,#e0e0e0 91px)"></div>
    <div class="panel" style="left:272px;top:11px;width:141px;height:217px"></div>
    <div class="ptitle" style="left:290px;top:40px;width:110px">Title subtitle + 2 rows and 2 columns of content (4 box)</div>
    <p class="lorem" style="left:290px;top:110px;width:110px">Lorem ipsum sit lom dolor sit amet, consectetur sit amet adipiscing. Lorem ipsum sit lom dolor sit amet, consectetur adipiscing<br><br>Lorem ipsum sit lom dolor sit amet, consectetur sit amet adipiscing. Lorem ipsum sit lom.</p>
    <div class="foot"><span>brankelladvisory.example</span><span>CONFIDENTIAL</span><span>14</span></div>
  </section>

  <section class="slide" style="left:946px;top:1617px">
    <div class="mark" style="left:30px;top:30px">BRANKELL</div>
    <div style="left:66px;top:27px;font-weight:800;font-size:9.5px;color:var(--ink)">TITLE 2 ROWS AND 2 COLUMNS OF CONTENT <small style="font-size:4.5px">(4 BOXES)</small></div>
    <div class="th" style="left:104px;top:68px;width:130px;height:27px">Columns 1</div>
    <div class="th" style="left:235px;top:68px;width:135px;height:27px">Columns 2</div>
    <div class="rh" style="left:42px;top:95px;width:62px;height:62px">Rows 1</div>
    <div class="rh" style="left:42px;top:158px;width:62px;height:63px">Rows 2</div>
    <div class="cell" style="left:104px;top:95px;width:266px;height:126px;background:linear-gradient(90deg,#e0e0e0 0 130px,#d6d6d6 130px 131px,#e0e0e0 131px)"></div>
    <div class="foot"><span>brankelladvisory.example</span><span>CONFIDENTIAL</span><span>15</span></div>
  </section>

  <!-- Row 6 -->
  <section class="slide" style="left:39px;top:1920px">
    <div class="panel" style="left:11px;top:11px;width:402px;height:95px"></div>
    <div class="mark w" style="left:28px;top:26px">BRANKELL</div>
    <div class="ptitle" style="left:30px;top:52px;width:360px">Nascar slide with comments</div>
    <p class="lorem" style="left:30px;top:67px;width:365px">Lorem ipsum sit lom dolor sit amet, consectetur sit amet adipiscing. Lorem ipsum sit lom dolor. Lorem ipsum sit lom dolor sit amet, consectetur sit amet adipiscing. Lorem ipsum sit lom dolor sit amet, consectetur sit amet adipiscing. Lorem ipsum sit lom dolor. Lorem ipsum sit lom dolor sit amet, consectetur sit amet adipiscing. Lorem ipsum sit lom dolor sit amet, consectetur adipiscing.</p>
    <div class="logo-v" style="left:61px;top:137px">VELTRIX</div>
    <div class="logo-b" style="left:138px;top:137px">BRANKELL</div>
    <div class="logo-v" style="left:216px;top:137px">VELTRIX</div>
    <div class="logo-b" style="left:293px;top:137px">BRANKELL</div>
    <div class="logo-v" style="left:371px;top:137px">VELTRIX</div>
    <div class="logo-b" style="left:61px;top:184px">BRANKELL</div>
    <div class="logo-v" style="left:138px;top:184px">VELTRIX</div>
    <div class="logo-b" style="left:216px;top:184px">BRANKELL</div>
    <div class="logo-v" style="left:293px;top:184px">VELTRIX</div>
    <div class="logo-b" style="left:371px;top:184px">BRANKELL</div>
    <div class="foot"><span>brankelladvisory.example</span><span>CONFIDENTIAL</span><span>16</span></div>
  </section>

  <section class="slide" style="left:492px;top:1918px">
    <div class="panel" style="left:11px;top:11px;width:134px;height:217px"></div>
    <div class="panel-gray" style="left:145px;top:11px;width:99px;height:217px"></div>
    <div class="mark w" style="left:28px;top:26px">BRANKELL</div>
    <div class="ptitle" style="left:30px;top:62px;width:100px">Data slide</div>
    <div class="dash" style="left:30px;top:78px"></div>
    <p class="lorem" style="left:30px;top:84px;width:100px">Lorem ipsum sit lom dolor sit amet, consectetur sit amet adipiscing. Lorem ipsum sit lom dolor. Lorem ipsum.<br><br>Lorem ipsum sit lom dolor sit amet, consectetur sit amet adipiscing. Lorem ipsum sit lom dolor. Lorem ipsum.<br><br>Lorem ipsum sit lom dolor sit amet, consectetur sit amet adipiscing. Lorem ipsum sit lom dolor. Lorem ipsum.</p>
    <svg style="left:145px;top:11px" width="99" height="217" viewBox="0 0 99 217"><g fill="none" stroke="#fff" stroke-width="1"><path d="M45 24 h9 M45 34 h9 M46 24 l7 10 M53 24 l-7 10"/><circle cx="49.5" cy="81" r="5"/><path d="M44.5 81 h10 M49.5 76 v10"/><circle cx="48" cy="129" r="4"/><path d="M51 132 l4 4"/></g></svg>
    <div class="icon-t" style="left:160px;top:51px"><b>TITLE HERE</b>Lorem ipsum sit lom dolor sit.</div>
    <div class="icon-t" style="left:160px;top:99px"><b>TITLE HERE</b>Lorem ipsum sit lom dolor sit.</div>
    <div class="icon-t" style="left:160px;top:149px"><b>TITLE HERE</b>Lorem ipsum sit lom dolor sit.</div>
    <svg style="left:258px;top:42px" width="124" height="124" viewBox="-62 -62 124 124">
      <g stroke="#fff" stroke-width="1.2">
        <path d="M0 0 L0 -60 A60 60 0 1 1 -34.4 49.1 Z" fill="#555"/>
        <path d="M0 0 L-34.4 49.1 A60 60 0 0 1 -56.4 -20.5 Z" fill="#a3a3a3"/>
        <path d="M0 0 L-56.4 -20.5 A60 60 0 0 1 -34.4 -49.1 Z" fill="#dadada"/>
        <path d="M0 0 L-34.4 -49.1 A60 60 0 0 1 0 -60 Z" fill="var(--blue)"/>
      </g>
    </svg>
    <div style="left:255px;top:178px;font-size:3.2px;color:#666;display:flex;gap:6px">
      <span>● 1st Qtr</span><span>● 2nd Qtr</span><span>● 3rd Qtr</span><span>● 4th Qtr</span>
    </div>
    <div class="foot"><span>brankelladvisory.example</span><span>CONFIDENTIAL</span><span>17</span></div>
  </section>

  <section class="slide" style="left:946px;top:1920px">
    <div class="panel" style="left:11px;top:11px;width:124px;height:217px"></div>
    <div class="panel-gray" style="left:135px;top:11px;width:68px;height:217px"></div>
    <div class="mark w" style="left:28px;top:26px">BRANKELL</div>
    <div class="ptitle" style="left:30px;top:64px;width:100px">Data slide</div>
    <p class="lorem" style="left:30px;top:82px;width:95px">Lorem ipsum sit lom dolor sit amet, consectetur sit amet adipiscing. Lorem ipsum sit lom dolor. Lorem ipsum.<br><br>Lorem ipsum sit lom dolor sit amet, consectetur sit amet adipiscing. Lorem ipsum sit lom dolor. Lorem ipsum.<br><br>Lorem ipsum sit lom dolor sit amet, consectetur sit amet adipiscing. Lorem ipsum sit lom dolor. Lorem ipsum.</p>
    <svg style="left:135px;top:11px" width="68" height="217" viewBox="0 0 68 217"><g fill="none" stroke="#fff" stroke-width="1"><path d="M30 24 h9 M30 34 h9 M31 24 l7 10 M38 24 l-7 10"/><circle cx="34" cy="81" r="5"/><path d="M29 81 h10 M34 76 v10"/><circle cx="33" cy="129" r="4"/><path d="M36 132 l4 4"/></g></svg>
    <div class="icon-t" style="left:134px;top:51px"><b>TITLE HERE</b>Lorem ipsum sit lom dolor sit.</div>
    <div class="icon-t" style="left:134px;top:99px"><b>TITLE HERE</b>Lorem ipsum sit lom dolor sit.</div>
    <div class="icon-t" style="left:134px;top:149px"><b>TITLE HERE</b>Lorem ipsum sit lom dolor sit.</div>
    <div style="left:270px;top:38px;font-size:5px;font-weight:600;color:#555">Chart Title</div>
    <svg style="left:215px;top:50px" width="198" height="150" viewBox="0 0 198 150">
      <g stroke="#e6e6e6" stroke-width=".5"><path d="M8 20 H190 M8 45 H190 M8 70 H190 M8 95 H190 M8 120 H190"/></g>
      <path d="M8 120 H190" stroke="#bbb" stroke-width=".6"/>
      <g fill="var(--blue)"><rect x="20" y="44" width="6" height="76"/><rect x="56" y="74" width="6" height="46"/><rect x="92" y="54" width="6" height="66"/><rect x="128" y="32" width="6" height="88"/></g>
      <g fill="#5f5f5f"><rect x="27" y="64" width="6" height="56"/><rect x="63" y="32" width="6" height="88"/><rect x="99" y="60" width="6" height="60"/><rect x="135" y="56" width="6" height="64"/></g>
      <g fill="#a5a5a5"><rect x="34" y="84" width="6" height="36"/><rect x="70" y="80" width="6" height="40"/><rect x="106" y="70" width="6" height="50"/><rect x="142" y="20" width="6" height="100"/></g>
      <g font-size="3.2" fill="#666" font-family="Montserrat,sans-serif"><text x="22" y="127">Category 1</text><text x="58" y="127">Category 2</text><text x="94" y="127">Category 3</text><text x="130" y="127">Category 4</text><text x="60" y="134">■ Series 1  ■ Series 2  ■ Series 3</text></g>
    </svg>
    <div class="foot"><span>brankelladvisory.example</span><span>CONFIDENTIAL</span><span>18</span></div>
  </section>

  <!-- Row 7 -->
  <section class="slide" style="left:39px;top:2213px">
    <div class="panel" style="left:11px;top:11px;width:124px;height:217px"></div>
    <div class="mark w" style="left:28px;top:26px">BRANKELL</div>
    <div class="ptitle" style="left:30px;top:64px;width:100px">Data slide</div>
    <p class="lorem" style="left:30px;top:82px;width:90px">Lorem ipsum sit lom dolor sit amet, consectetur sit amet<br><br>Lorem ipsum sit lom dolor sit amet, consectetur sit amet.<br><br>Lorem ipsum sit lom dolor sit amet, consectetur sit amet.<br><br>Lorem ipsum sit lom dolor sit amet, consectetur sit amet.</p>
    <div class="ring-label" style="left:205px;top:45px">CHART 1</div>
    <div class="ring-label" style="left:331px;top:45px">CHART 2</div>
    <div class="ring-label" style="left:206px;top:139px">CHART 3</div>
    <div class="ring-label" style="left:331px;top:139px">CHART 4</div>
    <svg style="left:0;top:0" width="425" height="238" viewBox="0 0 425 238">
      <g fill="none" stroke-width="4">
        <g stroke="#e4e4e4"><circle cx="205" cy="85" r="27"/><circle cx="331" cy="87" r="27"/><circle cx="206" cy="179" r="27"/><circle cx="331" cy="179" r="27"/></g>
        <g stroke="var(--blue)">
          <circle cx="205" cy="85" r="27" stroke-dasharray="34 170" transform="rotate(-90 205 85)"/>
          <circle cx="331" cy="87" r="27" stroke-dasharray="68 170" transform="rotate(-90 331 87)"/>
          <circle cx="206" cy="179" r="27" stroke-dasharray="25 170" transform="rotate(-90 206 179)"/>
          <circle cx="331" cy="179" r="27" stroke-dasharray="144 170" transform="rotate(-90 331 179)"/>
        </g>
      </g>
      <g fill="var(--blue)" font-family="Montserrat,sans-serif" font-weight="600" font-size="14" text-anchor="middle">
        <text x="205" y="90">20</text><text x="331" y="92">40</text><text x="206" y="184">15</text><text x="331" y="184">85</text>
      </g>
    </svg>
    <div class="foot"><span>brankelladvisory.example</span><span>CONFIDENTIAL</span><span>19</span></div>
  </section>

  <section class="slide" style="left:492px;top:2213px">
    <div class="panel" style="left:11px;top:11px;width:124px;height:217px"></div>
    <div class="mark w" style="left:28px;top:26px">BRANKELL</div>
    <div class="ptitle" style="left:30px;top:62px;width:100px">Editable infographic slide</div>
    <div class="dash" style="left:30px;top:98px"></div>
    <p class="lorem" style="left:30px;top:104px;width:95px">Lorem ipsum sit lom dolor sit amet, consectetur sit amet adipiscing. Lorem ipsum sit lom dolor. Lorem ipsum.<br><br>Lorem ipsum sit lom dolor sit amet, consectetur sit amet adipiscing. Lorem ipsum sit lom dolor. Lorem ipsum.</p>
    <svg style="left:0;top:0" width="425" height="238" viewBox="0 0 425 238"><circle cx="284" cy="127" r="74" fill="none" stroke="#e2e2e2" stroke-width="4"/></svg>
    <div class="box" style="left:245px;top:44px;width:78px;height:36px;background:#111"><b>Lorem Ipsum</b>• Some text here<br>• Some text here</div>
    <div class="box" style="left:180px;top:92px;width:76px;height:37px;background:#3a8fe0"><b>Lorem Ipsum</b>• Some text here<br>• Some text here</div>
    <div class="box" style="left:311px;top:92px;width:77px;height:37px;background:#6a6a6a"><b>Lorem Ipsum</b>• Some text here<br>• Some text here</div>
    <div class="box" style="left:205px;top:169px;width:78px;height:38px;background:#2a2a2a"><b>Lorem Ipsum</b>• Some text here<br>• Some text here</div>
    <div class="box" style="left:288px;top:169px;width:76px;height:38px;background:var(--blue-deep)"><b>Lorem Ipsum</b>• Some text here<br>• Some text here</div>
    <div class="foot"><span>brankelladvisory.example</span><span>CONFIDENTIAL</span><span>20</span></div>
  </section>

  <section class="slide" style="left:946px;top:2213px">
    <div class="mark" style="left:30px;top:28px">BRANKELL</div>
    <svg style="left:54px;top:32px" width="160" height="160" viewBox="-80 -80 160 160">
      <circle r="76" fill="none" stroke="#cfcfcf" stroke-width="3"/>
      <g stroke="#fff" stroke-width="2.5">
        <path d="M0 0 L0 -68 A68 68 0 0 1 64.7 -21 Z" fill="var(--blue)"/>
        <path d="M0 0 L64.7 -21 A68 68 0 0 1 40 55 Z" fill="#7a7a7a"/>
        <path d="M0 0 L40 55 A68 68 0 0 1 -40 55 Z" fill="#111"/>
        <path d="M0 0 L-40 55 A68 68 0 0 1 -64.7 -21 Z" fill="var(--blue-deep)"/>
        <path d="M0 0 L-64.7 -21 A68 68 0 0 1 0 -68 Z" fill="#7a7a7a"/>
      </g>
      <g fill="#fff" font-family="Montserrat,sans-serif" font-size="4.2" text-anchor="middle">
        <text x="22" y="-32" font-weight="600">Lorem Ipsum</text><text x="22" y="-27">• Some text here</text><text x="22" y="-22">• Some text here</text>
        <text x="36" y="9" font-weight="600">Lorem Ipsum</text><text x="36" y="14">• Some text here</text><text x="36" y="19">• Some text here</text>
        <text x="0" y="35" font-weight="600">Lorem Ipsum</text><text x="0" y="40">• Some text here</text><text x="0" y="45">• Some text here</text>
        <text x="-36" y="9" font-weight="600">Lorem Ipsum</text><text x="-36" y="14">• Some text here</text><text x="-36" y="19">• Some text here</text>
        <text x="-22" y="-32" font-weight="600">Lorem Ipsum</text><text x="-22" y="-27">• Some text here</text><text x="-22" y="-22">• Some text here</text>
      </g>
    </svg>
    <div class="panel" style="left:272px;top:11px;width:141px;height:217px"></div>
    <div class="ptitle" style="left:290px;top:54px;width:110px">Editable infographic slide</div>
    <div class="dash" style="left:290px;top:90px"></div>
    <p class="lorem" style="left:290px;top:96px;width:105px">Lorem ipsum sit lom dolor sit amet, consectetur sit amet adipiscing. Lorem ipsum sit lom dolor. Lorem ipsum.<br><br>Lorem ipsum sit lom dolor sit amet, consectetur sit amet adipiscing. Lorem ipsum sit lom dolor. Lorem ipsum.</p>
    <div class="foot"><span>brankelladvisory.example</span><span>CONFIDENTIAL</span><span>21</span></div>
  </section>

</div>
</body>
</html>
```